Information Technology Company needs a Website...

We need a single page website for new technology company called:

MERIDEL FALLS TECHNOLOGY GROUP
Based in Ojai CA.

We are offering three primary services:

- Business Solutions

- IT Services

- Software Implementation and Consulting

We want a single page design where all content scrolls down/up on one page. We're looking for the following characteristics:

- Home/Landing
- Active background with panoramic view (Will provide content)

- Business Solutions, IT Services, Software Implementation and Consulting

List of software vendors we recommend (Company logos)

- About
- History
- Our Team
- Partners

I'll upload our new logo as soon as we get the design files. I'll also send over some example website layout's that we like shortly.

Target Market(s)

Small/Medium Businesses

Industry/Entity Type

Information Technology

Number of Pages Required

1 page

Font styles to use
Other font styles liked:
• Sansation

Requirements
Must have
• Full page browser width, easy navigation and visibility. Creative design, not like every other "Technology" website template. Should be the "One Page" design where each section is below the next and the user scrolls down the page through the whole site. I like the concept of the following website in the main "Whiteboard" image:
• http://www.plavorix.com/design/4829137
• And the way this site does the active panoramic background:
• http://www.kelbrantworks.com/
• Something interesting and appealing to potential clients looking for Small/Medium business solutions and IT Services.
• Use uploaded Logo to establish color and theme for website.
Should not have
• Look the same as every other information technology website template.

```html
<!DOCTYPE html>
<html lang="en">
<head>
<meta charset="utf-8">
<title>Meridel Falls Technology Group</title>
<link href="https://fonts.googleapis.com/css2?family=Raleway:wght@400;500;600;700&display=swap" rel="stylesheet">
<style>
:root{
  --orange:#ef5a2f;
  --ink:#3a3a3a;
  --grey:#8e8e8e;
  --partner:#555555;
  --light:#e8e8e8;
  --white:#ffffff;
  --footer:#3d3d3d;
  --footer-text:#b3b3b3;
}
*{margin:0;padding:0;box-sizing:border-box}
html,body{width:1200px;height:2519px;overflow:hidden}
body{font-family:'Raleway',sans-serif;color:var(--ink);background:var(--white);position:relative}
section,header,footer{position:absolute;left:0;width:1200px}
.abs{position:absolute}
.center{text-align:center;left:0;width:1200px}

/* header */
.site-header{top:0;height:106px;background:var(--white)}
.brand{left:97px;top:36px;font-size:30px;font-weight:600;color:#555;letter-spacing:.5px}
.main-nav{right:102px;top:45px;display:flex;gap:42px;font-size:19px;font-weight:600;color:var(--ink)}
.main-nav .active{color:var(--orange)}

/* hero */
.hero{top:106px;height:519px}
.hero-bg{position:absolute;inset:0;background:linear-gradient(100deg,#2a1d16 0%,#4a3324 45%,#6b4a32 70%,#3a2a20 100%)}
.hero-shade{position:absolute;inset:0;background:linear-gradient(90deg,rgba(0,0,0,.35),rgba(0,0,0,.05))}
.hero-title{left:97px;top:138px;font-size:42px;font-weight:600;line-height:55px;color:var(--orange)}
.hero-text{left:97px;top:264px;width:640px;font-size:25px;line-height:34px;color:var(--white)}

/* welcome */
.welcome{top:625px;height:596px;background:var(--light)}
.section-title{font-size:27px;font-weight:600;color:var(--ink);letter-spacing:.5px}
.intro{font-size:15.5px;line-height:29px;color:var(--grey);left:100px;width:1000px;text-align:center}
.service{width:260px;text-align:center}
.service-icon{width:112px;height:112px;border:2px solid var(--orange);border-radius:50%;margin:0 auto;background:var(--white);display:flex;align-items:center;justify-content:center}
.service-name{margin-top:30px;font-size:17px;font-weight:600;color:var(--orange)}
.service-text{margin-top:28px;font-size:13px;line-height:19px;color:var(--grey)}

/* history */
.history{top:1221px;height:379px}
.history-bg{position:absolute;inset:0;background:linear-gradient(90deg,#1c1c1a 0%,#2c2a24 40%,#3a3526 60%,#1e1d1b 100%)}
.history-shade{position:absolute;inset:0;background:rgba(0,0,0,.45)}
.history .section-title{color:var(--white)}
.history-text{left:170px;width:860px;text-align:center;font-size:17.5px;line-height:36px;color:var(--white)}
.btn-outline{left:505px;top:277px;width:197px;height:50px;border:1.5px solid var(--white);color:var(--white);font-size:14px;font-weight:600;display:flex;align-items:center;justify-content:center;letter-spacing:.3px}

/* team */
.team{top:1600px;height:613px;background:var(--light)}
.member{width:240px;text-align:center}
.member-photo{width:180px;height:180px;border-radius:50%;margin:0 auto}
.member-name{margin-top:38px;font-size:26px;font-weight:600;color:var(--orange)}
.member-role{margin-top:6px;font-size:15px;color:var(--grey)}

/* partners */
.partners{top:2213px;height:176px;background:var(--white)}
.partner{top:66px;height:40px;width:280px;display:flex;align-items:center;justify-content:center;gap:12px;font-size:26px;font-weight:600;color:var(--partner);white-space:nowrap}
.partner-mark{width:28px;height:28px;background:#c9c9c9;flex:none}
.partner-mark.round{border-radius:50%}

/* footer */
.site-footer{top:2389px;height:130px;background:var(--footer)}
.footer-nav{left:48px;top:38px;font-size:15px;font-weight:600;color:var(--footer-text);word-spacing:4px}
.copyright{left:48px;top:76px;font-size:15px;font-weight:600;color:var(--footer-text)}
.social-label{left:605px;top:56px;font-size:15px;font-weight:600;color:var(--footer-text)}
.social{top:50px;display:flex;gap:22px;left:940px;font-size:15px;font-weight:600;color:var(--footer-text)}
</style>
</head>
<body>

<header class="site-header">
  <div class="abs brand">Meridel Falls</div>
  <nav class="abs main-nav">
    <span class="active">HOME</span><span>ABOUT US</span><span>HISTORY</span><span>OUR TEAM</span><span>PARTNERS</span>
  </nav>
</header>

<section class="hero">
  <div class="hero-bg" role="img" aria-label="Night-time panoramic view of a city skyline with lit office towers"></div>
  <div class="hero-shade"></div>
  <h1 class="abs hero-title">Welcome to Meridel Falls<br>Technology Group</h1>
  <p class="abs hero-text">Lorem ipsum dolor sit amet, consectetur adipiscing elit, sed do eiusmod tempor incididunt ut labore et dolore magna aliqua. Ut enim ad minim veniam,.</p>
</section>

<section class="welcome">
  <h2 class="abs center section-title" style="top:60px">WELCOME TO MERIDEL FALLS</h2>
  <p class="abs intro" style="top:115px">Lorem ipsum dolor sit amet, consectetur adipiscing elit, sed do eiusmod tempor incididunt ut labore et dolore magna aliqua. Ut enim ad minim veniam, quis nostrud exercitation ullamco laboris nisi ut aliquip ex ea commodo consequat. Duis aute irure dolor in reprehenderit in voluptate velit esse cillum dolore eu fugiat nulla pariatur.</p>

  <div class="abs service" style="left:66px;top:256px">
    <div class="service-icon">
      <svg width="50" height="50" viewBox="0 0 50 50" fill="var(--orange)">
        <circle cx="25" cy="17" r="8"/>
        <path d="M10 46 C10 32 18 28 25 28 C32 28 40 32 40 46 Z"/>
        <path d="M25 2v4M14 6l3 3M36 6l-3 3" stroke="var(--orange)" stroke-width="2"/>
      </svg>
    </div>
    <div class="service-name">BUSINESS SOLUTIONS</div>
    <p class="service-text">Lorem ipsum dolor sit amet, consectetur adipiscing elit, sed do eiusmod tempor incididunt ut labore et cillum dolore eu fugiat nulla pariatur.</p>
  </div>

  <div class="abs service" style="left:470px;top:256px">
    <div class="service-icon">
      <svg width="56" height="44" viewBox="0 0 56 44" fill="none" stroke="var(--orange)" stroke-width="3">
        <rect x="8" y="4" width="40" height="28" rx="2"/>
        <path d="M2 38h52"/>
        <path d="M26 12l6 10-3 0 2 4" stroke-width="2"/>
      </svg>
    </div>
    <div class="service-name">IT SERVICES</div>
    <p class="service-text">Lorem ipsum dolor sit amet, consectetur adipiscing elit, sed do eiusmod tempor incididunt ut labore et cillum dolore eu fugiat nulla pariatur.</p>
  </div>

  <div class="abs service" style="left:874px;top:256px">
    <div class="service-icon">
      <svg width="56" height="46" viewBox="0 0 56 46" fill="none" stroke="var(--orange)" stroke-width="3">
        <rect x="4" y="4" width="40" height="30" rx="2"/>
        <path d="M4 11h40"/>
        <path d="M12 18l5 4-5 4M20 27h8" stroke-width="2"/>
        <circle cx="44" cy="34" r="7" fill="var(--white)"/>
        <circle cx="44" cy="34" r="2" fill="var(--orange)"/>
      </svg>
    </div>
    <div class="service-name">SOFTWARE DEVELOPMENT</div>
    <p class="service-text">Lorem ipsum dolor sit amet, consectetur adipiscing elit, sed do eiusmod tempor incididunt ut labore et cillum dolore eu fugiat nulla pariatur.</p>
  </div>
</section>

<section class="history">
  <div class="history-bg" role="img" aria-label="Dim office interior with a man seated on a sofa"></div>
  <div class="history-shade"></div>
  <h2 class="abs center section-title" style="top:58px">HISTORY</h2>
  <p class="abs history-text" style="top:126px">Lorem Ipsum is simply dummy text of the printing and typesetting industry. Lorem Ipsum has been the industry's standard dummy text ever since the 1500s, when an unknown printer took a galley of type and scrambled it to make a type specimen book.</p>
  <div class="abs btn-outline">READ MORE INFO</div>
</section>

<section class="team">
  <h2 class="abs center section-title" style="top:57px">OUR TEAM</h2>
  <p class="abs intro" style="top:112px">Lorem ipsum dolor sit amet, consectetur adipiscing elit, sed do eiusmod tempor incididunt ut labore et dolore magna aliqua. Ut enim ad minim veniam, quis nostrud exercitation ullamco laboris nisi ut aliquip ex ea commodo consequat.</p>

  <div class="abs member" style="left:67px;top:230px">
    <div class="member-photo" role="img" aria-label="Portrait of team member Lena Hartwell" style="background:radial-gradient(circle at 50% 45%,#c89068,#6a3a22)"></div>
    <div class="member-name">LENA HARTWELL</div>
    <div class="member-role">WEB DESIGNER</div>
  </div>
  <div class="abs member" style="left:342px;top:230px">
    <div class="member-photo" role="img" aria-label="Portrait of team member Nora Ellison" style="background:radial-gradient(circle at 50% 60%,#e0d4cc,#f4f0ee)"></div>
    <div class="member-name">NORA ELLISON</div>
    <div class="member-role">WEB DEVELOPER</div>
  </div>
  <div class="abs member" style="left:616px;top:230px">
    <div class="member-photo" role="img" aria-label="Portrait of team member Evan Crosby" style="background:radial-gradient(circle at 50% 45%,#9a9a9a,#3c3c3c)"></div>
    <div class="member-name">EVAN CROSBY</div>
    <div class="member-role">SOFTWARE DEVELOPER</div>
  </div>
  <div class="abs member" style="left:891px;top:230px">
    <div class="member-photo" role="img" aria-label="Portrait of team member Owen Tallis" style="background:radial-gradient(circle at 50% 75%,#d8463a,#f2eeec 70%)"></div>
    <div class="member-name">OWEN TALLIS</div>
    <div class="member-role">SOFTWARE ANALYST</div>
  </div>
</section>

<section class="partners">
  <div class="abs partner" style="left:43px"><span class="partner-mark round"></span>Solvanta</div>
  <div class="abs partner" style="left:345px"><span class="partner-mark"></span>Leaspire</div>
  <div class="abs partner" style="left:632px"><span class="partner-mark"></span>Corvel Brainworks</div>
  <div class="abs partner" style="left:912px"><span class="partner-mark round"></span>Geovanta</div>
</section>

<footer class="site-footer">
  <div class="abs footer-nav">HOME &nbsp;/&nbsp; ABOUT US &nbsp;/&nbsp; HISTORY &nbsp;/&nbsp; OUR TEAM &nbsp;/&nbsp; PARTNERS</div>
  <div class="abs copyright">COPYRIGHT © 2016. ALL RIGHTS RESERVED</div>
  <div class="abs social-label">CONNECT WITH OUR SOCIAL NETWORK:</div>
  <div class="abs social"><span>Fablr</span><span>Chirpo</span><span>Linkora</span></div>
</footer>

</body>
</html>
```